Excel Template (Branded)

I have a number of reports that I create in Excel. I would like them to be branded instead of generic. Creating a template that I could use for all of my reports would be ideal. I would like to use the colours and logo of my website quillborne.ca for branding ideas.

Target Market(s)

Everyday investors over the age of 18

Industry/Entity Type

investment

Requirements
Must have
• Professional design that will be shared with readers and subscribers of my blog
Nice to have
• clean professional design elements

```html
<!DOCTYPE html>
<html lang="en">
<head>
<meta charset="utf-8">
<title>10YR Compound Annual Growth Rates – Quillborne</title>
<link rel="stylesheet" href="https://fonts.googleapis.com/css2?family=Carlito:wght@400;700&family=Arimo:wght@400;700&display=swap">
<style>
  :root {
    --blue: #4f81bd;
    --blue-dark: #375f93;
    --row-a: #b8cce4;
    --row-b: #dce6f1;
    --rule: #7f7f7f;
    --title: #2f5597;
    --green: #0e8f4f;
    --note-bg: #f0f0f0;
    --note-text: #404040;
    --white: #ffffff;
  }
  * { margin: 0; padding: 0; box-sizing: border-box; }
  html, body { width: 1200px; height: 692px; overflow: hidden; background: var(--white); }
  .sheet { position: relative; width: 1200px; height: 692px; font-family: "Carlito", "Calibri", sans-serif; }

  .brand { position: absolute; left: 26px; top: 48px; display: flex; align-items: center; gap: 8px; }
  .brand-dot { width: 30px; height: 30px; border-radius: 50%; background: var(--blue-dark); }
  .brand-name { font-weight: 700; font-size: 27px; color: var(--blue-dark); }

  .title { position: absolute; left: 224px; width: 941px; top: 24px; text-align: center;
           font-weight: 700; font-size: 26px; color: var(--title); }

  .band { position: absolute; top: 68px; height: 44.5px; color: var(--white); font-weight: 700;
          display: flex; align-items: center; justify-content: center; gap: 12px; font-size: 17px; }
  .band-growth { left: 224px; width: 520px; background: var(--blue); }
  .band-price { left: 746px; width: 102px; background: var(--blue-dark); }
  .band-yield { left: 850px; width: 155px; background: var(--blue); }
  .band-total { left: 1007px; width: 158px; background: var(--blue-dark); align-items: flex-start;
                padding-top: 8px; font-size: 17px;
                clip-path: polygon(0 0, 150px 0, 158px 8px, 158px 100%, 0 100%); }
  .band-icon { width: 26px; height: 26px; }
  .cagr-tabs { position: absolute; left: 1007px; top: 97px; width: 158px; height: 15.5px; display: flex; }
  .cagr-tabs span { flex: 1; color: var(--white); font-weight: 700; font-size: 11px; text-align: center;
                    border-left: 1px solid var(--white); line-height: 16px; background: var(--blue-dark);
                    clip-path: polygon(0 0, calc(100% - 4px) 0, 100% 4px, 100% 100%, 0 100%); }
  .cagr-tabs span:first-child { border-left: 0; }

  .head-row { position: absolute; top: 123px; left: 19.5px; height: 21px; display: flex;
              font-family: "Arimo", Arial, sans-serif; font-weight: 700; color: var(--white); font-size: 8.5px; }
  .head-row span { display: flex; align-items: center; justify-content: center; width: 52.5px;
                   background: var(--blue); border-right: 1px solid var(--white); }
  .head-row .col-symbol { width: 52.5px; }
  .head-row .col-company { width: 148px; justify-content: flex-start; padding-left: 3px; font-size: 12px; }
  .head-row .dark { background: var(--blue-dark); }

  .grid { position: absolute; top: 146px; left: 19.5px; width: 1145.5px; height: 431px;
          background:
            repeating-linear-gradient(to bottom, transparent 0 17px, var(--white) 17px 17.96px),
            repeating-linear-gradient(to bottom, var(--row-a) 0 17.96px, var(--row-b) 17.96px 35.92px); }
  .grid-cols { position: absolute; top: 146px; left: 220px; width: 945px; height: 431px;
               background: repeating-linear-gradient(to right, transparent 0 51.5px, rgba(255,255,255,.7) 51.5px 52.5px); }
  .rule-light { position: absolute; top: 146px; left: 71.5px; width: 1px; height: 431px; background: rgba(255,255,255,.7); }
  .rule { position: absolute; top: 146px; width: 1px; height: 431px; background: var(--rule); }

  .averages { position: absolute; top: 585px; left: 19.5px; width: 827.5px; height: 30px; background: var(--green);
              color: var(--white); font-weight: 700; font-size: 20px; display: flex; align-items: center;
              justify-content: center; }
  .avg-cells { position: absolute; top: 587px; left: 848px; width: 317px; height: 29px; display: flex; gap: 1px; }
  .avg-cells span { flex: 1; background: var(--green); }

  .note { position: absolute; top: 630px; left: 19px; width: 1141px; height: 62px; background: var(--note-bg);
          padding: 4px 6px; color: var(--note-text); font-weight: 700; font-size: 13.3px; line-height: 17.5px; }
</style>
</head>
<body>
<div class="sheet">
  <div class="brand"><span class="brand-dot"></span><span class="brand-name">Quillborne</span></div>
  <h1 class="title">10YR-Compound Annual Growth Rates (CAGR) as of 01-01-2021</h1>

  <div class="band band-growth">Ten Years of Dividend Growth (Year-by-Year)
    <svg class="band-icon" viewBox="0 0 26 26" fill="none" stroke="#fff" stroke-width="2"><path d="M13 24V12M13 16c-4 0-6-2-6-5 3 0 6 2 6 5zM13 16c4 0 6-2 6-5-3 0-6 2-6 5z"/><text x="13" y="9" fill="#fff" stroke="none" font-size="10" text-anchor="middle" font-weight="700">$</text></svg>
  </div>
  <div class="band band-price">Price
    <svg class="band-icon" viewBox="0 0 26 26" fill="none" stroke="#fff" stroke-width="2"><circle cx="13" cy="13" r="11"/><circle cx="13" cy="13" r="7.5"/><text x="13" y="17" fill="#fff" stroke="none" font-size="11" text-anchor="middle" font-weight="700">$</text></svg>
  </div>
  <div class="band band-yield">Yield
    <svg class="band-icon" viewBox="0 0 26 26" fill="none" stroke="#fff" stroke-width="1.6"><circle cx="13" cy="13" r="11.5"/><path d="M9 18v-3M12 18v-5M15 18v-7M8 12l6-5M11 7h3v3"/></svg>
  </div>
  <div class="band band-total">Total return</div>
  <div class="cagr-tabs"><span>CAGR</span><span>CAGR</span><span>CAGR</span></div>

  <div class="head-row">
    <span class="col-symbol">Symbol</span><span class="col-company">Company</span>
    <span>2011</span><span>2012</span><span>2013</span><span>2014</span><span>2015</span>
    <span>2016</span><span>2017</span><span>2018</span><span>2019</span><span>2020</span>
    <span class="dark">$'11</span><span class="dark">$'21</span>
    <span>YLD'11</span><span>YLD'21</span><span>10YOC</span>
    <span class="dark">10Y TR</span><span class="dark">10Y DG</span><span class="dark">10Y PG</span>
  </div>

  <div class="grid"></div>
  <div class="grid-cols"></div>
  <div class="rule-light"></div>
  <div class="rule" style="left:220px"></div>
  <div class="rule" style="left:745px"></div>
  <div class="rule" style="left:850px"></div>
  <div class="rule" style="left:1007.5px"></div>

  <div class="averages">Averages</div>
  <div class="avg-cells"><span></span><span></span><span></span><span></span><span></span><span></span></div>

  <div class="note">
    <p>As successful dividend growth investors we understand that rising dividends are a foundation for higher share prices.</p>
    <p>Here is the Compound Annual Growth Rate (CAGR) of dividends and CAGR of price over the last decade so that you can study the&nbsp; evidence that as the dividend grows, so does the price</p>
  </div>
</div>
</body>
</html>
```